Social Media Application Design - Android and IOS

I am ready to go live with new social media app however I am not comfortable with the current design. It is a not interactive or attractive enough. Please note the splash screen is a green, so preference would be to keep a green theme although I am more than happy to consider other colours that would improve the design.
The attachment has the app screens that need to be redesigned. They may not need massive changes , however keen to go live so looking for inspired designers to support with this project and many others that I have, including ongoing work on this app.
Target Market(s)
Millenials
Industry/Entity Type
Social
Colors
Designer to choose colors to be used in the design.
Requirements
Must have
- Please see attached document for screens that I would like redesigned. It needs to work with Android and IOS. I am looking for the design and not the functionality.
Nice to have
- Highly interactive design. Please see polling functionality of Pictavo.
Should not have
- should not be complicated - simplicity is the key

```html
<!DOCTYPE html>
<html lang="en">
<head>
<meta charset="utf-8">
<title>Ask App – Screens</title>
<link href="https://fonts.googleapis.com/css2?family=Montserrat:wght@400;500;600;700&display=swap" rel="stylesheet">
<style>
:root{
  --canvas:#ffffff;
  --paper:#f7f6f2;
  --ink:#2f2f2f;
  --ink-soft:#555555;
  --muted:#9a9a9a;
  --line:#dcdad4;
  --amber:#f8a21b;
  --orange:#fa8a0f;
  --yellow:#fdc90a;
  --chip-line:#f3a23a;
  --olive:rgba(120,95,20,.55);
}
*{box-sizing:border-box;margin:0;padding:0}
html,body{width:1200px;height:797px;overflow:hidden;background:var(--canvas)}
body{position:relative;font-family:'Montserrat',sans-serif;color:var(--ink)}
.screen{position:absolute;top:73px;width:375px;height:813px;transform:scale(.8);transform-origin:0 0;
  background:var(--paper);border-radius:44px;overflow:hidden;box-shadow:0 10px 30px rgba(0,0,0,.12)}
.screen--menu{left:64px}
.screen--compose{left:459px}
.screen--topics{left:855px}
.abs{position:absolute}

/* menu */
.profile-cover{position:absolute;left:0;top:0;width:375px;height:396px;
  background:linear-gradient(160deg,#e98a12 0%,#e9a018 45%,#e6b51c 100%)}
.close-btn{left:22px;top:42px}
.avatar{left:27px;top:211px;width:88px;height:88px;border-radius:50%;border:2px solid rgba(255,255,255,.7);
  background:linear-gradient(135deg,#6b5646,#c7a78a 60%,#8a8480)}
.profile-name{left:25px;top:322px;font-size:24px;font-weight:700;color:#fff;letter-spacing:.5px}
.profile-mail{left:25px;top:357px;font-size:15px;color:#fff;letter-spacing:.3px;opacity:.95}
.menu-item{position:absolute;left:0;width:375px;height:66px}
.menu-item .icon{position:absolute;left:13px;top:22px}
.menu-item .label{position:absolute;left:49px;top:23px;font-size:15px;font-weight:500;letter-spacing:.5px;color:var(--ink)}
.menu-item.has-rule::after{content:"";position:absolute;left:38px;right:10px;bottom:0;height:1px;background:var(--line)}
.badge{position:absolute;left:160px;top:22px;width:36px;height:22px;border-radius:11px;background:var(--amber);
  color:#fff;font-size:11px;font-weight:700;text-align:center;line-height:22px}
.toggle{position:absolute;left:314px;top:24px;width:38px;height:20px}
.toggle::before{content:"";position:absolute;left:0;top:7px;width:30px;height:6px;border-radius:3px;background:#f7c46a}
.toggle::after{content:"";position:absolute;right:0;top:0;width:20px;height:20px;border-radius:50%;background:var(--amber)}
.home-bar{position:absolute;left:120px;bottom:8px;width:135px;height:4px;border-radius:2px;background:#fff;opacity:.8}

/* shared header */
.app-bar{position:absolute;left:0;top:0;width:375px;background:linear-gradient(120deg,var(--yellow) 0%,var(--amber) 60%,var(--orange) 100%)}
.app-bar .back{position:absolute;left:19px;top:42px}
.app-bar .title{position:absolute;left:0;right:0;top:47px;text-align:center;font-size:15px;font-weight:600;color:#fff;letter-spacing:.4px}
.app-bar .action{position:absolute;right:17px;top:47px;font-size:15px;font-weight:700;color:#fff;letter-spacing:.4px}

.heading{position:absolute;left:23px;font-size:24px;font-weight:700;letter-spacing:1.2px;line-height:30px;color:var(--ink)}
.heading--lg{line-height:37px}

.chip{position:absolute;height:38px;border-radius:19px;font-size:15px;font-weight:700;letter-spacing:.5px;
  display:flex;align-items:center;justify-content:center;white-space:nowrap}
.chip--on{background:linear-gradient(90deg,var(--orange),var(--yellow));color:#fff}
.chip--off{border:1.5px solid var(--chip-line);color:var(--ink);background:transparent}

.question-box{left:23px;top:338px;width:324px;height:179px;border:1.5px solid var(--line);border-radius:6px;
  padding:10px 13px;font-size:12px;font-weight:500;color:var(--muted);letter-spacing:.4px}
.select{left:23px;top:631px;width:324px;height:49px;border:1.5px solid var(--line);border-radius:6px;
  padding:15px 13px;font-size:12px;font-weight:500;color:var(--muted);letter-spacing:.4px}
.select svg{position:absolute;right:14px;top:21px}
.upload{position:absolute;top:718px;width:70px;height:69px;border:1.5px dashed var(--line);border-radius:6px;
  display:flex;align-items:center;justify-content:center}

.search{left:50px;top:105px;width:275px;height:42px;border-radius:21px;background:var(--olive);
  display:flex;align-items:center;justify-content:center;gap:14px;font-size:12px;color:rgba(255,255,255,.75);letter-spacing:.5px}
</style>
</head>
<body>

<!-- Side menu -->
<section class="screen screen--menu">
  <div class="profile-cover" role="img" aria-label="Profile cover photo in warm amber tones"></div>
  <svg class="abs close-btn" width="12" height="12" viewBox="0 0 12 12"><path d="M1 1l10 10M11 1L1 11" stroke="#fff" stroke-width="2.4" stroke-linecap="round"/></svg>
  <div class="abs avatar" role="img" aria-label="Profile photo"></div>
  <div class="abs profile-name">Marlon Reyes</div>
  <div class="abs profile-mail">marlon.reyes@mailora.com</div>

  <nav>
    <div class="menu-item has-rule" style="top:403px">
      <svg class="icon" width="14" height="14" viewBox="0 0 14 14"><path d="M1 7L7 1l6 6v6H1z" fill="#9a9a9a"/></svg>
      <span class="label">Home</span>
    </div>
    <div class="menu-item has-rule" style="top:469px">
      <svg class="icon" width="14" height="14" viewBox="0 0 14 14"><circle cx="7" cy="4" r="3.2" fill="#9a9a9a"/><path d="M1.5 13c0-3 2.5-4.5 5.5-4.5s5.5 1.5 5.5 4.5z" fill="#9a9a9a"/></svg>
      <span class="label">My Profile</span>
    </div>
    <div class="menu-item has-rule" style="top:535px">
      <svg class="icon" width="14" height="14" viewBox="0 0 14 14"><rect x="1" y="6" width="2.4" height="7" fill="#9a9a9a"/><rect x="5.5" y="3" width="2.4" height="10" fill="#9a9a9a"/><rect x="10" y="8" width="2.4" height="5" fill="#9a9a9a"/></svg>
      <span class="label">My Activities</span>
    </div>
    <div class="menu-item has-rule" style="top:601px">
      <svg class="icon" width="14" height="14" viewBox="0 0 14 14"><path d="M2 11c1.5-1 1.5-3 1.5-5a3.5 3.5 0 017 0c0 2 0 4 1.5 5z" fill="#9a9a9a"/><circle cx="7" cy="12.5" r="1.3" fill="#9a9a9a"/></svg>
      <span class="label">Notifications</span>
      <span class="badge">9+</span>
      <span class="toggle"></span>
    </div>
    <div class="menu-item has-rule" style="top:668px">
      <svg class="icon" width="14" height="14" viewBox="0 0 14 14"><path d="M3 1l2.5 3-1.5 2c1 2 2 3 4 4l2-1.5 3 2.5-1.5 2C6 12.5 1.5 8 1 2.5z" fill="#9a9a9a"/></svg>
      <span class="label">Contact Us</span>
    </div>
    <div class="menu-item" style="top:734px">
      <svg class="icon" width="15" height="14" viewBox="0 0 15 14"><path d="M8 1H1.5v12H8" fill="none" stroke="#9a9a9a" stroke-width="1.5"/><path d="M5 7h9M11 4l3 3-3 3" fill="none" stroke="#9a9a9a" stroke-width="1.5"/></svg>
      <span class="label">Log Out</span>
    </div>
  </nav>
  <div class="home-bar" style="background:#ddd"></div>
</section>

<!-- Compose question -->
<section class="screen screen--compose">
  <header class="app-bar" style="height:85px">
    <svg class="back" width="28" height="18" viewBox="0 0 28 18"><path d="M27 9H2M9 1.5L1.5 9 9 16.5" fill="none" stroke="#fff" stroke-width="2.4" stroke-linecap="round" stroke-linejoin="round"/></svg>
    <div class="title">Post a Question</div>
    <div class="action">Post</div>
  </header>

  <h2 class="heading" style="top:103px">Your Question<br>Is about</h2>
  <div class="chip chip--on" style="left:23px;top:181px;width:132px;height:40px">Technology</div>
  <div class="chip chip--on" style="left:167px;top:181px;width:101px;height:40px">Health</div>
  <div class="chip chip--on" style="left:281px;top:179px;width:100px;height:40px">Religion</div>

  <h2 class="heading heading--lg" style="top:255px">What is your<br>Question?</h2>
  <div class="abs question-box">Type question ...</div>

  <h2 class="heading heading--lg" style="top:540px">What are the<br>Options?</h2>
  <div class="abs select">Images
    <svg width="10" height="6" viewBox="0 0 10 6"><path d="M1 1l4 4 4-4" fill="none" stroke="#333" stroke-width="1.4"/></svg>
  </div>

  <div class="upload" style="left:23px"><svg width="26" height="20" viewBox="0 0 26 20"><path d="M2 5h6l2-3h6l2 3h6v13H2z" fill="none" stroke="#c9c7c1" stroke-width="1.5"/><circle cx="13" cy="11" r="4" fill="none" stroke="#c9c7c1" stroke-width="1.5"/></svg></div>
  <div class="upload" style="left:108px"><svg width="26" height="20" viewBox="0 0 26 20"><path d="M2 5h6l2-3h6l2 3h6v13H2z" fill="none" stroke="#c9c7c1" stroke-width="1.5"/><circle cx="13" cy="11" r="4" fill="none" stroke="#c9c7c1" stroke-width="1.5"/></svg></div>
  <div class="upload" style="left:193px"><svg width="26" height="20" viewBox="0 0 26 20"><path d="M2 5h6l2-3h6l2 3h6v13H2z" fill="none" stroke="#c9c7c1" stroke-width="1.5"/><circle cx="13" cy="11" r="4" fill="none" stroke="#c9c7c1" stroke-width="1.5"/></svg></div>
  <div class="upload" style="left:278px"><svg width="18" height="18" viewBox="0 0 18 18"><path d="M9 1v16M1 9h16" stroke="#c9c7c1" stroke-width="2.2"/></svg></div>
  <div class="home-bar" style="background:#ddd"></div>
</section>

<!-- Topic picker -->
<section class="screen screen--topics">
  <header class="app-bar" style="height:164px">
    <svg class="back" width="28" height="18" viewBox="0 0 28 18"><path d="M27 9H2M9 1.5L1.5 9 9 16.5" fill="none" stroke="#fff" stroke-width="2.4" stroke-linecap="round" stroke-linejoin="round"/></svg>
    <div class="title">Post a Question</div>
    <div class="action">Next</div>
    <div class="abs search">
      <svg width="18" height="18" viewBox="0 0 18 18"><circle cx="7" cy="7" r="5.5" fill="none" stroke="#fff" stroke-width="2"/><path d="M11 11l5.5 5.5" stroke="#fff" stroke-width="2.4" stroke-linecap="round"/></svg>
      <span>Search topic</span>
    </div>
  </header>

  <h2 class="heading" style="top:186px">What is<br>your Question about ?</h2>

  <div class="chip chip--off" style="left:24px;top:285px;width:100px">Science</div>
  <div class="chip chip--on"  style="left:145px;top:284px;width:119px">Technology</div>
  <div class="chip chip--off" style="left:298px;top:285px;width:100px">Gedget</div>

  <div class="chip chip--on"  style="left:-20px;top:363px;width:101px;justify-content:flex-end;padding-right:24px">Health</div>
  <div class="chip chip--off" style="left:92px;top:363px;width:105px">Fashion</div>
  <div class="chip chip--off" style="left:215px;top:363px;width:95px">Beauty</div>
  <div class="chip chip--off" style="left:325px;top:363px;width:90px">Travel</div>

  <div class="chip chip--on"  style="left:78px;top:463px;width:100px">Travel</div>
  <div class="chip chip--off" style="left:190px;top:463px;width:104px">Religion</div>
  <div class="chip chip--off" style="left:308px;top:463px;width:96px">History</div>

  <div class="chip chip--off" style="left:-6px;top:557px;width:97px">Language</div>
  <div class="chip chip--off" style="left:102px;top:557px;width:106px">Education</div>
  <div class="chip chip--off" style="left:221px;top:557px;width:95px">Business</div>
  <div class="chip chip--off" style="left:332px;top:557px;width:90px">Finance</div>

  <div class="chip chip--off" style="left:7px;top:652px;width:100px">Finance</div>
  <div class="chip chip--on"  style="left:121px;top:652px;width:123px">My&nbsp;&nbsp;Country</div>
  <div class="chip chip--off" style="left:256px;top:652px;width:96px">My Cities</div>
  <div class="home-bar" style="background:#ddd"></div>
</section>

</body>
</html>
```